Talent Agency Needs Identity!

We are Copper Gate Artists Inc. - a full service entertainment services agency that focuses primarily on securing contracts for musicians and entertainers aboard luxury cruise ships, however we are not limited exclusively to that area, as we are expanding into the areas of film and television.

We are looking for the perfect website and logo from the right designer!

We already own the domain www.coppergateartists.example

The homepage only needs to be designed for this contest, unless you really want to go that extra mile!

Would like full HTML and CSS3 if applicable.

Logo needs to be designed as well.

We have two primary colors that we want to use - Lime green and grey (or charcoal, slate, graphite etc.)

The pages should be mostly slate colored background, slightly peppered with green accents, tastefully incorporated.

The key target audience of the website will be artists and musicians seeking representation, but also entertainment executives sourcing our talent. We are focused on a refined, legitimate, clever image.

Some ideas for pages we have:
Home Page
About Us
Life At Sea
Apply Now
Contact Us
FAQ
Members Only Section

Some ideas for inspiration can be found at:
www.varnoagency.example
www.pelbrooktunes.example
www.tidewarden.example
www.keelmark.example
www.dravelent.example

The logo needs to be designed as well.

The logo should be simple, and communicate creativity, legitimacy, and current trends. Just a simple word logo. "Copper Gate Artists", again with a refined, professional look and feel, with elements of creativity and cleverness incorporated.

We plan to expand into the areas of film and television - so this can be considered in the final design, which is why we have chosen the name Copper Gate to begin with.

The term Copper Gate in the context of the film industry means to formally approve a project's production finance, thereby allowing the project to move forward from the development phase to pre-production and principal photography.

Therefore, we want our image to be 'forward thinking and feeling'.

The website should be SEO optimized and include the following keywords:

cruise ship music gigs musicians jobs

Target Market(s)

Musicians, entertainment executives/buyers

Industry/Entity Type

Entertainment

Requirements
Must have
• Simple, easy to navigate design. An example of a website far too complicated:
www.quarbyworks.example

An example of a nice, clean website we like:
www.varnoagency.example
www.dravelent.example
www.keelmark.example
Nice to have
• A members only section where talent can log in to see their recruitment info.

A page for talent buyers.

A clean, enticing home page, leaving you curious to explore.

Should not have
• A busy, difficult to navigate interface.

Cheesy looking clip art.

```html
<!DOCTYPE html>
<html lang="en">
<head>
<meta charset="utf-8">
<title>Copper Gate Artists – Cruise Ship Music Gigs &amp; Musicians Jobs</title>
<meta name="description" content="Copper Gate Artists places musicians in cruise ship music gigs and musicians jobs around the world.">
<link rel="stylesheet" href="https://fonts.googleapis.com/css2?family=Ubuntu:wght@400;700&family=Roboto+Condensed:wght@400&family=Lilita+One&display=swap">
<style>
  :root {
    --lime: #4cae12;
    --lime-dark: #0f8a0c;
    --lime-text: #3fa519;
    --charcoal: #262626;
    --frame: #3b3b3b;
    --ink: #111111;
    --paper: #ffffff;
    --muted: #7c7c7c;
    --orange-top: #ff8a1e;
    --orange-bot: #e2530a;
    --bulb: #c6ee2a;
  }
  * { box-sizing: border-box; margin: 0; padding: 0; }
  html, body { width: 1200px; height: 1125px; overflow: hidden; }
  body {
    position: relative;
    font-family: Arial, Helvetica, sans-serif;
    background: #1a1a1a;
  }
  .backdrop {
    position: absolute; inset: 0;
    background: linear-gradient(160deg, #121212 0%, #3a3a3a 35%, #9a9a9a 70%, #cfcfcf 100%);
  }
  .site { position: absolute; left: 141px; top: 32px; width: 919px; height: 943px; background: var(--frame); }
  .masthead {
    position: absolute; left: 0; top: 0; width: 919px; height: 102px;
    background: linear-gradient(180deg, var(--lime) 0%, var(--lime-dark) 100%);
  }
  .brand { position: absolute; left: 17px; top: 32px; display: flex; align-items: center; gap: 10px; }
  .brand-dot { width: 30px; height: 30px; border-radius: 50%; background: var(--bulb); }
  .brand-name { font-family: 'Ubuntu', sans-serif; font-weight: 700; font-size: 22px; color: var(--paper); }
  .callout {
    position: absolute; right: 11px; top: 10px;
    font-family: 'Lilita One', sans-serif; font-size: 25px; color: #f4d98a;
    text-shadow: 0 0 2px #6a3b00, 1px 1px 0 #6a3b00, -1px -1px 0 #6a3b00;
    letter-spacing: .5px;
  }
  .nav { position: absolute; right: 11px; top: 62px; display: flex; font-family: 'Ubuntu', sans-serif; font-size: 15px; color: var(--ink); }
  .nav a { color: var(--ink); text-decoration: none; }
  .nav a.current { border-bottom: 1px solid var(--ink); }
  .nav .sep { margin: 0 9px; }
  .stage { position: absolute; left: 14px; top: 117px; width: 891px; height: 812px; background: var(--charcoal); }
  .hero { position: absolute; left: 0; top: 0; width: 891px; height: 374px;
    background: radial-gradient(ellipse at 50% 60%, #b1283a 0%, #4a1530 40%, #120a1a 80%), #111; }
  .hero-dots { position: absolute; right: 16px; bottom: 10px; display: flex; gap: 7px; }
  .hero-dots span { width: 10px; height: 10px; border-radius: 50%; background: var(--paper); }
  .hero-dots span.active { background: #7fc21c; }
  .caption { position: absolute; left: 0; top: 374px; width: 891px; height: 66px; background: var(--ink);
    font-family: 'Roboto Condensed', sans-serif; font-size: 18px; color: #d9d9d9; padding: 22px 15px; }
  .categories { position: absolute; left: 6px; top: 453px; display: flex; gap: 14px; }
  .category { width: 209px; height: 173px; background: #0c0c0c; position: relative; }
  .category-photo { height: 86px; }
  .tone-stage { background: linear-gradient(90deg, #b0461c 0%, #5b2a2a 45%, #7b2fb8 75%, #a45ce8 100%); }
  .tone-singers { background: linear-gradient(90deg, #2a0505 0%, #b03020 40%, #d9a080 70%, #1a0a08 100%); }
  .tone-cellists { background: linear-gradient(90deg, #1d2a22 0%, #8a9a8a 30%, #1a221c 50%, #8a9a8a 75%, #1a221c 100%); }
  .category h3 { font-family: 'Roboto Condensed', sans-serif; font-weight: 400; font-size: 17px; color: var(--lime-text);
    text-align: center; margin-top: 6px; line-height: 20px; }
  .category p { font-size: 11px; line-height: 16px; color: var(--muted); padding: 0 7px; }
  .category .more { position: absolute; right: 10px; bottom: 6px; font-size: 10px; color: var(--lime-text); text-decoration: none; }
  .careers-title { position: absolute; left: 7px; top: 641px; font-family: 'Ubuntu', sans-serif; font-weight: 400; font-size: 16px; color: var(--lime-text); }
  .rule { position: absolute; left: 9px; top: 669px; width: 870px; border-top: 2px dotted #5a5a5a; }
  .careers-copy { position: absolute; left: 10px; top: 680px; width: 872px; font-size: 11.2px; line-height: 17.8px; color: var(--paper); }
  .careers-copy p + p { margin-top: 15px; width: 660px; }
  .apply {
    position: absolute; left: 699px; top: 744px; width: 176px; height: 54px; border-radius: 3px;
    background: linear-gradient(180deg, var(--orange-top), var(--orange-bot));
    border: 1px solid #ffb36b;
    font-family: 'Ubuntu', sans-serif; font-size: 23px; color: var(--paper); text-align: center; line-height: 52px; text-decoration: none;
  }
  .footer-note { position: absolute; left: 141px; top: 997px; font-size: 11.5px; color: var(--ink); }
  .social { position: absolute; left: 911px; top: 989px; display: flex; gap: 9px; }
  .social span { width: 23px; height: 23px; border-radius: 3px; background: #3c6fb3; }
  .social span:nth-child(2) { background: #5fb6e0; }
  .social span:nth-child(3) { background: #1e5a9c; }
  .social span:nth-child(4) { background: #222; }
  .social span:nth-child(5) { background: #3aa847; }
</style>
</head>
<body>
  <div class="backdrop" role="img" aria-label="Black and white close-up of piano keys"></div>

  <div class="site">
    <header class="masthead">
      <div class="brand"><span class="brand-dot"></span><span class="brand-name">Copper Gate Artists</span></div>
      <div class="callout">Call us @ 1-877-555-0142</div>
      <nav class="nav">
        <a class="current" href="#">Home</a><span class="sep">/</span>
        <a href="#">About us</a><span class="sep">/</span>
        <a href="#">Life at Sea</a><span class="sep">/</span>
        <a href="#">Apply Now</a><span class="sep">/</span>
        <a href="#">Contact us</a><span class="sep">/</span>
        <a href="#">Faq</a><span class="sep">/</span>
        <a href="#">Member Zone</a>
      </nav>
    </header>

    <main class="stage">
      <div class="hero" role="img" aria-label="Band of musicians with guitars posing on a lit stage">
        <div class="hero-dots"><span></span><span class="active"></span><span></span></div>
      </div>
      <div class="caption">Lorem Ipsum is simply dummy text of the</div>

      <section class="categories">
        <article class="category">
          <div class="category-photo tone-stage" role="img" aria-label="Theatre stage with purple curtain"></div>
          <h3>CATEGORY NAME</h3>
          <p>Lorem Ipsum is simply dummy text of the printing and typesetting industry. Lorem Ipsum has...</p>
          <a class="more" href="#">Read more...</a>
        </article>
        <article class="category">
          <div class="category-photo tone-singers" role="img" aria-label="Singers performing at a microphone"></div>
          <h3>CATEGORY NAME</h3>
          <p>Lorem Ipsum is simply dummy text of the printing and typesetting industry. Lorem Ipsum has...</p>
          <a class="more" href="#">Read more...</a>
        </article>
        <article class="category">
          <div class="category-photo tone-cellists" role="img" aria-label="String players performing"></div>
          <h3>CATEGORY NAME</h3>
          <p>Lorem Ipsum is simply dummy text of the printing and typesetting industry. Lorem Ipsum has...</p>
          <a class="more" href="#">Read more...</a>
        </article>
        <article class="category">
          <div class="category-photo tone-stage" role="img" aria-label="Theatre stage with purple curtain"></div>
          <h3>CATEGORY NAME</h3>
          <p>Lorem Ipsum is simply dummy text of the printing and typesetting industry. Lorem Ipsum has...</p>
          <a class="more" href="#">Read more...</a>
        </article>
      </section>

      <h2 class="careers-title">Exciting Careers At Sea</h2>
      <div class="rule"></div>
      <div class="careers-copy">
        <p>We offer a range of representation services--all designed to help you reach your potential. We place musicians on luxury cruise ships sailing on exotic itineraries all over the world, as well as in world class venue's such as Las Vegas hotels, casino's, and theaters. We have partnered with the world's leading cruise lines and have direct access to the jobs you want.</p>
        <p>Whatever your situation - if you're thinking about your first gig on a cruise ship, or perhaps making a move to a new cruise line or position, we are on the front lines and work to get you what you want at a rate you deserve.</p>
      </div>
      <a class="apply" href="#">Apply Now</a>
    </main>
  </div>

  <footer>
    <p class="footer-note">Copyright © 2012. COPPERGATEARTISTS.EXAMPLE. All rights reserved.</p>
    <div class="social" aria-label="Social links"><span></span><span></span><span></span><span></span><span></span></div>
  </footer>
</body>
</html>
```